Flyer for Car Detailing Shop

I am opening a detailing shop. I am looking for a nice, easy to read single sided flyer I can hand out at car shows, hang in store windows and to my clients and customers to promote my business. I want it a little professional yet attention grabbing. I want someone to look at it and go "holy shit, thats a nice flyer" haha

Here are some things that must be included:
- Company Name: Brightfern Motorworks Detailing & Coatings
- Tag Line: The Science of Detailing
- Address: 4150 Harlow Rd, Temperance, MI 48190
- www.brightfernmotor.example
- Find Us on social Media! ::insert facebook and instagram logo
Colors: Black, Lime Green and Purple for accents, etc

HAND WASH
- Express Wash start at $25
- Deluxe Wash Start at $50

EXTERIOR DETAILING
-Basic Packages Start at $160
- Deluxe Packages Start at $350

INTERIOR DETAILING
- Basic Packages Start at $60
- Deluxe Packages Start at $200

New Car Prep and Ceramic Coatings
*Consultation required prior to beginning work*
- Paint: Starting at $500
- Interior: Starting at $100
- Wheels Off: Starting at $200
- Trim: Starting at $100
- Windows: $50 windshield/ $25 per pane

Additional Services
- Scratch removal
- Ozone Treatment
- Headlight Restoration
- Chip Repair

```html
<!DOCTYPE html>
<html lang="en">
<head>
<meta charset="utf-8">
<title>Brightfern Motorworks Detailing &amp; Coatings – Flyer</title>
<link href="https://fonts.googleapis.com/css2?family=Montserrat:ital,wght@0,400;0,500;0,600;0,700;0,800;1,500;1,700;1,800&display=swap" rel="stylesheet">
<style>
  :root {
    --lime: #6dd46a;
    --lime-dark: #4fb84c;
    --ink: #1f1f1f;
    --panel: #262626;
    --paper: #ffffff;
    --text: #222222;
    --rule: #9a9a9a;
    --muted: #555555;
  }
  * { box-sizing: border-box; margin: 0; padding: 0; }
  html, body { width: 900px; height: 1200px; overflow: hidden; background: #eeeeee; }
  body { font-family: "Montserrat", Arial, sans-serif; color: var(--text); }

  .flyer { position: relative; width: 900px; height: 1200px; background: var(--paper); overflow: hidden; }

  .hero-band { position: absolute; left: 0; top: 0; width: 900px; height: 770px; background: var(--lime); }
  .hero-panel { position: absolute; left: 0; top: 0; }

  .headline { position: absolute; left: 76px; top: 56px; line-height: 1; text-transform: uppercase; }
  .headline__name { display: block; color: #fff; font-weight: 800; font-size: 54px; letter-spacing: 0.5px; margin-bottom: 6px; }
  .headline__service { display: block; color: var(--lime); font-weight: 600; font-size: 54px; letter-spacing: 0.5px; margin-top: 8px; }

  .brand-mark { position: absolute; left: 612px; top: 120px; width: 190px; display: flex; flex-direction: column; align-items: center; gap: 12px; }
  .brand-mark__dot { width: 46px; height: 46px; border-radius: 50%; border: 3px solid #fff; }
  .brand-mark__name { color: #fff; font-weight: 700; font-size: 19px; text-align: center; line-height: 1.2; }

  .photo { position: absolute; }
  .photo--vehicle { left: 268px; top: 290px; width: 594px; height: 320px; border-radius: 120px 160px 40px 60px; background: radial-gradient(ellipse at 50% 45%, #f3f3f3 0%, #cfcfcf 55%, #6c6c6c 100%); }
  .photo--technician { left: 52px; top: 300px; width: 196px; height: 470px; border-radius: 90px 90px 0 0; background: linear-gradient(180deg, #c9b8a6 0%, #b7b7b7 28%, #2e3f6e 48%, #1f2c52 100%); }

  .web-line { position: absolute; left: 300px; top: 628px; display: flex; align-items: center; gap: 16px; }
  .web { color: var(--lime); font-weight: 700; font-style: italic; font-size: 22px; white-space: nowrap; }
  .web-icon { flex: none; display: block; }

  .tagline { position: absolute; left: 258px; top: 702px; font-size: 47px; font-weight: 800; font-style: italic; color: var(--ink); letter-spacing: -0.5px; white-space: nowrap; }

  .menu { position: absolute; top: 790px; }
  .menu--left { left: 47px; width: 348px; }
  .menu--right { left: 437px; width: 421px; }

  .section-tab { display: inline-block; position: relative; background: var(--lime); color: #fff; font-weight: 700; font-size: 18px; letter-spacing: 0.5px; padding: 5px 34px 5px 12px; clip-path: polygon(0 0, 100% 0, calc(100% - 14px) 100%, 0 100%); text-transform: uppercase; }
  .section-tab--wide { width: 100%; text-transform: none; font-size: 18px; }

  .price-list { list-style: none; margin-top: 10px; margin-bottom: 22px; }
  .price-row { display: flex; align-items: baseline; font-size: 16px; font-weight: 500; height: 28px; }
  .price-row__leader { flex: 1; border-bottom: 1px solid var(--rule); margin: 0 8px; transform: translateY(-3px); }
  .price-row__price { min-width: 44px; text-align: right; }
  .price-pair { display: flex; gap: 30px; text-align: right; position: relative; }
  .price-pair__item { position: relative; }
  .price-pair__item small { position: absolute; top: 20px; font-size: 10px; white-space: nowrap; color: var(--muted); }
  .price-pair__item--first small { left: 50%; transform: translateX(-50%); }
  .price-pair__item--last small { right: 0; }

  .note { font-size: 12px; font-weight: 500; margin-top: 10px; }
  .menu--right .price-list { margin-top: 8px; }
  .menu--right .price-row { height: 30px; }

  .extras { position: relative; margin-top: 26px; border: 1.5px solid var(--ink); border-radius: 12px; height: 84px; padding: 22px 18px 0; }
  .extras__title { position: absolute; top: -12px; left: 14px; background: var(--paper); padding: 0 8px; font-size: 17px; font-weight: 600; }
  .extras__list { list-style: none; display: grid; grid-template-columns: 1fr 1fr; row-gap: 8px; font-size: 15px; font-weight: 500; }
  .extras__list li { display: flex; align-items: center; gap: 8px; }
  .extras__list li::before { content: ""; width: 10px; height: 10px; border-radius: 50%; background: var(--lime); }

  .footer { position: absolute; left: 45px; top: 1132px; width: 820px; height: 58px; background: var(--ink); border-radius: 12px 12px 0 0; display: flex; align-items: center; padding: 0 24px; color: #fff; gap: 18px; }
  .footer__address { font-style: italic; font-weight: 500; font-size: 23px; white-space: nowrap; }
  .footer__divider { width: 2px; height: 30px; background: var(--lime); }
  .footer__social { display: flex; align-items: center; gap: 12px; font-weight: 600; font-size: 19px; white-space: nowrap; }
  .footer__social-dot { width: 20px; height: 20px; border-radius: 50%; border: 2px solid #fff; }
</style>
</head>
<body>
<main class="flyer">
  <div class="hero-band"></div>
  <svg class="hero-panel" width="900" height="770" viewBox="0 0 900 770">
    <path d="M60 24 H790 Q822 24 822 56 V560 L720 679 H28 V56 Q28 24 60 24 Z" fill="var(--panel)"/>
  </svg>

  <h1 class="headline">
    <span class="headline__name">Brightfern</span>
    <span class="headline__name">Motorworks</span>
    <span class="headline__service">Detailing &amp;</span>
    <span class="headline__service">Coatings</span>
  </h1>

  <div class="brand-mark">
    <span class="brand-mark__dot"></span>
    <span class="brand-mark__name">Brightfern Motorworks</span>
  </div>

  <div class="photo photo--vehicle" role="img" aria-label="Photo of a white compact SUV, three-quarter front view"></div>
  <div class="photo photo--technician" role="img" aria-label="Photo of a detailer in navy overalls and gloves, arms crossed"></div>

  <div class="web-line">
    <p class="web">www.brightfernmotor.example</p>
    <svg class="web-icon" width="30" height="30" viewBox="0 0 30 30" aria-hidden="true">
      <rect x="1" y="1" width="28" height="28" rx="5" fill="#fff" stroke="var(--ink)" stroke-width="1.5"/>
      <circle cx="15" cy="15" r="8" fill="none" stroke="var(--ink)" stroke-width="1.6"/>
      <ellipse cx="15" cy="15" rx="3.5" ry="8" fill="none" stroke="var(--ink)" stroke-width="1.4"/>
      <line x1="7" y1="15" x2="23" y2="15" stroke="var(--ink)" stroke-width="1.4"/>
    </svg>
  </div>

  <p class="tagline">The Science of Detailing</p>

  <section class="menu menu--left">
    <h2 class="section-tab">Hand Wash</h2>
    <ul class="price-list">
      <li class="price-row"><span>Express Wash start at</span><span class="price-row__leader"></span><span class="price-row__price">$25</span></li>
      <li class="price-row"><span>Deluxe Wash Start at</span><span class="price-row__leader"></span><span class="price-row__price">$50</span></li>
    </ul>
    <h2 class="section-tab">Exterior Detailing</h2>
    <ul class="price-list">
      <li class="price-row"><span>Basic Packages Start at</span><span class="price-row__leader"></span><span class="price-row__price">$160</span></li>
      <li class="price-row"><span>Deluxe Packages Start at</span><span class="price-row__leader"></span><span class="price-row__price">$350</span></li>
    </ul>
    <h2 class="section-tab">Interior Detailing</h2>
    <ul class="price-list">
      <li class="price-row"><span>Basic Packages Start at</span><span class="price-row__leader"></span><span class="price-row__price">$60</span></li>
      <li class="price-row"><span>Deluxe Packages Start at</span><span class="price-row__leader"></span><span class="price-row__price">$200</span></li>
    </ul>
  </section>

  <section class="menu menu--right">
    <h2 class="section-tab section-tab--wide">New Car Prep and Ceramic Coatings</h2>
    <p class="note">Consultation required prior to beginning work</p>
    <ul class="price-list">
      <li class="price-row"><span>Paint: Starting at</span><span class="price-row__leader"></span><span class="price-row__price">$500</span></li>
      <li class="price-row"><span>Interior: Starting at</span><span class="price-row__leader"></span><span class="price-row__price">$100</span></li>
      <li class="price-row"><span>Wheels Off: Starting at</span><span class="price-row__leader"></span><span class="price-row__price">$200</span></li>
      <li class="price-row"><span>Trim: Starting at</span><span class="price-row__leader"></span><span class="price-row__price">$100</span></li>
      <li class="price-row"><span>Windows:</span><span class="price-row__leader"></span>
        <span class="price-pair">
          <span class="price-pair__item price-pair__item--first">$50<small>Windshield</small></span>
          <span class="price-pair__item price-pair__item--last">$25<small>Per pane</small></span>
        </span>
      </li>
    </ul>
    <div class="extras">
      <h3 class="extras__title">Additional Services</h3>
      <ul class="extras__list">
        <li>Scratch removal</li>
        <li>Headlight Restoration</li>
        <li>Ozone Treatment</li>
        <li>Chip Repair</li>
      </ul>
    </div>
  </section>

  <footer class="footer">
    <span class="footer__address">4150 Harlow Rd, Temperance, MI 48190</span>
    <span class="footer__divider"></span>
    <span class="footer__social"><span class="footer__social-dot"></span>Brightfern Motorworks</span>
  </footer>
</main>
</body>
</html>
```